SKVC Stationary and business Card
SKVC letterhead and Business Card
Professional
Summit Kinship Vitality Center
Dr. Marcus Pellham, D.C. Dr. Tamsin Pellham, D.C.
2948 Arden Avenue Boulder, CO 80304
drpellham@summitvitalityclinics.com
www.summitvitalityclinics.com

```html
<!DOCTYPE html>
<html lang="en">
<head>
<meta charset="utf-8">
<title>SKVC Business Card Set</title>
<link href="https://fonts.googleapis.com/css2?family=Cinzel:wght@400;600&family=Cormorant+SC:wght@500&display=swap" rel="stylesheet">
<style>
  :root {
    --backdrop: #ece8e2;
    --card-white: #ffffff;
    --purple: #8b6aa9;
    --purple-deep: #6d4e8f;
    --purple-light: #a98cc4;
    --ink: #5a4a68;
    --label: #2e2a2a;
    --ghost: rgba(139,106,169,0.08);
    --ghost-light: rgba(255,255,255,0.12);
  }
  * { box-sizing: border-box; margin: 0; padding: 0; }
  html, body { width: 1200px; height: 794px; overflow: hidden; }
  body {
    background: var(--backdrop);
    font-family: "Cormorant SC", serif;
    position: relative;
  }
  .card {
    position: absolute;
    width: 408px; height: 264px;
    border-radius: 16px;
    overflow: hidden;
    box-shadow: 0 2px 6px rgba(0,0,0,0.18);
  }
  .card--white { background: var(--card-white); color: var(--ink); }
  .card--purple {
    background: radial-gradient(ellipse at 55% 40%, var(--purple-light) 0%, var(--purple) 55%, var(--purple-deep) 100%);
    color: #fff;
  }
  .front-a { left: 101px; top: 43px; }
  .front-b { left: 643px; top: 43px; }
  .back-a  { left: 101px; top: 413px; }
  .back-b  { left: 643px; top: 413px; }

  .side-band { position: absolute; top: 0; bottom: 0; left: 26px; width: 34px; }
  .card--white .side-band {
    background: linear-gradient(90deg, var(--purple) 0 6px, transparent 6px 10px, var(--purple) 10px 100%);
  }
  .card--purple .side-band {
    background: linear-gradient(90deg, #fff 0 6px, transparent 6px 10px, #fff 10px 100%);
    opacity: 0.95;
  }
  .ghost-mark {
    position: absolute; right: -40px; top: 30px;
    width: 210px; height: 210px; border-radius: 50%;
  }
  .card--white .ghost-mark { background: var(--ghost); }
  .card--purple .ghost-mark { background: var(--ghost-light); }

  .brand { position: absolute; left: 70px; top: 14px; font-family: "Cinzel", serif; font-weight: 600; }
  .card--white .brand { color: var(--purple); }
  .brand-line-1 { font-size: 25px; letter-spacing: 0.5px; line-height: 1; }
  .brand-line-2 { font-size: 14px; letter-spacing: 3.5px; line-height: 1.2; margin-left: 4px; }

  .doctors { position: absolute; left: 78px; top: 96px; font-size: 11px; line-height: 1.35; letter-spacing: 0.3px; }
  .contact { position: absolute; left: 78px; top: 180px; list-style: none; font-size: 9.5px; line-height: 1.5; letter-spacing: 0.3px; }
  .contact li { display: flex; align-items: center; gap: 6px; }
  .contact svg { width: 8px; height: 8px; flex: none; }

  .back-mark {
    position: absolute; left: 0; right: 0; top: 92px;
    display: flex; flex-direction: column; align-items: center; gap: 8px;
    font-family: "Cinzel", serif; font-weight: 600; font-size: 18px; letter-spacing: 3px;
  }
  .back-mark .dot { width: 44px; height: 44px; border-radius: 50%; }
  .card--white .back-mark { color: var(--purple); }
  .card--white .back-mark .dot { background: var(--purple); }
  .card--purple .back-mark .dot { background: #fff; }
  .back-url {
    position: absolute; left: 0; right: 0; bottom: 22px; text-align: center;
    font-size: 9px; letter-spacing: 3px;
  }
  .card--white .back-url { color: #8a8090; }

  .caption {
    position: absolute; width: 408px; text-align: center;
    font-family: "Cinzel", serif; font-weight: 400; font-size: 21px; letter-spacing: 1.5px;
    color: var(--label);
  }
</style>
</head>
<body>

<section class="card card--white front-a">
  <div class="ghost-mark"></div>
  <div class="side-band"></div>
  <div class="brand"><div class="brand-line-1">Summit Kinship</div><div class="brand-line-2">Vitality Center</div></div>
  <div class="doctors"><p>Dr. Marcus Pellham, D.C.</p><p>Dr. Tamsin Pellham, D.C.</p></div>
  <ul class="contact">
    <li><svg viewBox="0 0 8 8"><rect x="2" y="0" width="4" height="8" rx="1" fill="currentColor"/></svg>303.555.0142</li>
    <li><svg viewBox="0 0 8 8"><rect x="0" y="2" width="8" height="5" fill="currentColor"/></svg>303.555.0187</li>
    <li><svg viewBox="0 0 8 8"><path d="M4 0 8 4H7V8H1V4H0Z" fill="currentColor"/></svg>2948 Arden Avenue Boulder, CO 80304</li>
    <li><svg viewBox="0 0 8 8"><circle cx="4" cy="4" r="3.5" fill="currentColor"/></svg>drpellham@summitvitalityclinics.com</li>
    <li><svg viewBox="0 0 8 8"><circle cx="4" cy="4" r="3" fill="none" stroke="currentColor"/></svg>www.summitvitalityclinics.com</li>
  </ul>
</section>

<section class="card card--purple front-b">
  <div class="ghost-mark"></div>
  <div class="side-band"></div>
  <div class="brand"><div class="brand-line-1">Summit Kinship</div><div class="brand-line-2">Vitality Center</div></div>
  <div class="doctors"><p>Dr. Marcus Pellham, D.C.</p><p>Dr. Tamsin Pellham, D.C.</p></div>
  <ul class="contact">
    <li><svg viewBox="0 0 8 8"><rect x="2" y="0" width="4" height="8" rx="1" fill="currentColor"/></svg>303.555.0142</li>
    <li><svg viewBox="0 0 8 8"><rect x="0" y="2" width="8" height="5" fill="currentColor"/></svg>303.555.0187</li>
    <li><svg viewBox="0 0 8 8"><path d="M4 0 8 4H7V8H1V4H0Z" fill="currentColor"/></svg>2948 Arden Avenue Boulder, CO 80304</li>
    <li><svg viewBox="0 0 8 8"><circle cx="4" cy="4" r="3.5" fill="currentColor"/></svg>drpellham@summitvitalityclinics.com</li>
    <li><svg viewBox="0 0 8 8"><circle cx="4" cy="4" r="3" fill="none" stroke="currentColor"/></svg>www.summitvitalityclinics.com</li>
  </ul>
</section>

<p class="caption" style="left:101px; top:352px;">Business Card Front A</p>
<p class="caption" style="left:643px; top:352px;">Business Card Front B</p>

<section class="card card--white back-a">
  <div class="back-mark"><span class="dot"></span>SKVC</div>
  <p class="back-url">www.summitvitalityclinics.com</p>
</section>

<section class="card card--purple back-b">
  <div class="back-mark"><span class="dot"></span>SKVC</div>
  <p class="back-url">www.summitvitalityclinics.com</p>
</section>

<p class="caption" style="left:101px; top:736px;">Business Card Back A</p>
<p class="caption" style="left:643px; top:736px;">Business Card Back B</p>

</body>
</html>
```